New healthy snacks brand

We are launching a brand new product with an innovative new concept.
The product is an outer carton box which contains 4 inner plastic punnets, each containing a different type of dry snack.
The brand identity is, healthy, environmentally friendly, convenient, simple and cool. The target customers are 25-50 year old healthy conscious medium to high income office workers.
The name is amber wayfare.

Outer box:
The outer box will be made of brown recycled carton. The dimensions are to be approximately that of an A4 paper, 21cmX30cmX3cm height.
The top side of the cover is to be as uncluttered as possible and to contain only the logo and the recyclable symbol.

The inside of the top cover is to contain a drawing/picture relevant to the brand identity.
The bottom side is to contain the following:
-The top left area of 4 cm X 10 cm is to be left blank to allow for a sticker with address, and name of the recipient of this specific box.
- The top right area (4cm X 20cm) is to contain mini logos for the following claims along with the wording itself:
- Gluten free - Cholesterol free - Soy free - Lactose free - natural - vegan - No high fructose corn syrup - No artificial flavours - 0g transfat - No artificial sweeteners - no partially hydrogenated oil.

Inner containers:
There will be 4 inner plastic containers arranged in a square formation (see pictures). Each container is to have a transparent label adhered to its oval top containing the following:
- Brand logo
- Name of the type of snack inside.
- The barcode
-In fine print the list if ingredients.
- The printing is to be in one colour only to allow ease of viewing the contents of the punnet.
For more clarifications please see the attached pictures of the blank packaging samples.

Target Market(s)

25 - 50 year old healthy conscious professionals.

Industry/Entity Type

Plastic

Requirements
Must have
• The design must be as simple as possible using one maximum 2 earthy colours.

```html
<!DOCTYPE html>
<html lang="en">
<head>
<meta charset="utf-8">
<title>amber wayfare – container labels</title>
<link rel="stylesheet" href="https://fonts.googleapis.com/css2?family=Josefin+Sans:ital,wght@0,300;0,400;1,300&family=Arimo&display=swap">
<style>
  :root {
    --page: #ffffff;
    --outline: #cfcfcf;
    --label-base: #d3dcdb;
    --green: #a3c54a;
    --yellow: #d9b425;
    --orange: #ea5c24;
    --blue: #4a8bcb;
    --heading: #8a6a52;
    --note: #111111;
    --fine: #1c1c1c;
  }
  * { margin: 0; padding: 0; box-sizing: border-box; }
  html, body { width: 1200px; height: 784px; overflow: hidden; background: var(--page); }
  .sheet { position: relative; width: 1200px; height: 784px; }
  .punnets { position: absolute; left: 0; top: 0; }
  .punnet-outline { fill: none; stroke: var(--outline); stroke-width: 1.2; }
  .label-area { fill: var(--label-base); }
  .ink-fill { fill: var(--ink); }
  .ink-stroke { stroke: var(--ink); fill: none; }
  .brand-name { font-family: "Josefin Sans", sans-serif; font-weight: 400; font-size: 23px; fill: var(--ink); }
  .snack-name { font-family: "Josefin Sans", sans-serif; font-weight: 300; font-size: 17px; fill: var(--ink); }
  .ingredients-title { font-family: "Josefin Sans", sans-serif; font-style: italic; font-weight: 300; font-size: 10px; fill: var(--ink); }
  .ingredients-fine { font-family: "Arimo", sans-serif; font-size: 7.5px; fill: var(--fine); }
  .label--green { --ink: var(--green); }
  .label--yellow { --ink: var(--yellow); }
  .label--orange { --ink: var(--orange); }
  .label--blue { --ink: var(--blue); }
  .section-title {
    position: absolute; left: 906px; top: 608px;
    font-family: "Josefin Sans", sans-serif; font-weight: 400; font-size: 29px;
    color: var(--heading);
  }
  .design-notes {
    position: absolute; left: 568px; top: 664px;
    font-family: "Arimo", sans-serif; font-size: 14px; line-height: 17.5px;
    color: var(--note); list-style: none;
  }
</style>
</head>
<body>
<main class="sheet">
  <svg class="punnets" width="1200" height="600" viewBox="0 0 1200 600" aria-label="Four punnet lid labels">
    <defs>
      <symbol id="punnet-lid" viewBox="0 0 402 282" width="402" height="282">
        <path class="punnet-outline" d="M201,1 C345,1 401,45 401,141 C401,237 345,281 201,281 C57,281 1,237 1,141 C1,45 57,1 201,1 Z"/>
        <path class="label-area" d="M204,30 C315,30 363,62 363,133 C363,204 315,236 204,236 C93,236 45,204 45,133 C45,62 93,30 204,30 Z"/>
        <g class="brand-mark">
          <circle class="ink-fill" cx="141" cy="96" r="6"/>
          <text class="brand-name" x="141" y="134" text-anchor="middle">amber</text>
          <text class="brand-name" x="141" y="160" text-anchor="middle">wayfare</text>
        </g>
        <line class="ink-stroke" x1="203" y1="80" x2="203" y2="197" stroke-width="1.4"/>
        <text class="snack-name" x="213" y="94">Snack-name</text>
        <text class="ingredients-title" x="213" y="108">Ingredients :</text>
        <rect class="ink-fill" x="213" y="112" width="102" height="50"/>
        <text class="ingredients-fine" x="264" y="140" text-anchor="middle">print ingredients here</text>
        <g class="recycle-icon" stroke-width="3" stroke-linecap="round">
          <path class="ink-stroke" d="M299,175 L293,185"/>
          <path class="ink-stroke" d="M306,175 L312,185"/>
          <path class="ink-stroke" d="M296,194 L309,194"/>
          <polygon class="ink-fill" points="302,170 308,177 298,178"/>
          <polygon class="ink-fill" points="315,189 312,197 307,190"/>
          <polygon class="ink-fill" points="290,190 294,196 297,187"/>
        </g>
      </symbol>
    </defs>
    <use href="#punnet-lid" class="label--green" x="197" y="10"/>
    <use href="#punnet-lid" class="label--yellow" x="623" y="10"/>
    <use href="#punnet-lid" class="label--orange" x="197" y="307"/>
    <use href="#punnet-lid" class="label--blue" x="623" y="307"/>
  </svg>

  <h1 class="section-title">Container</h1>

  <ul class="design-notes">
    <li>*You didn't describe diameter of container.</li>
    <li>&nbsp;So, this parts should be corrected via farther info.</li>
    <li>*Light blue color of back is there for the its position. not to be color. It should be transparent.</li>
    <li>*Colors are just suggestion. If you wish to be one color for all four boxes,</li>
    <li>&nbsp;it should be Green or Orange.</li>
  </ul>
</main>
</body>
</html>
```